Office Building Banner

Need a 4x8 vinyl banner made for our office/storage headquarters. Our branded colors and logo can be taken from our website, www.halvenroofingtx.com. All other elements of our brand have not been decided on yet, so you have creative autonomy there. Our location faces a busy highway in Seguin, Texas, so the banner needs to have our contact information and full name clearly seen from a bit away's away, hope that makes sense. Our company wants to convey attributes of strength, loyalty, protection - basically emulating the qualities of a wolf and his pack. I have uploaded a few items we have been using to date, but as you can see, graphic design is not our forte.

```html
<!DOCTYPE html>
<html lang="en">
<head>
<meta charset="utf-8">
<title>Halven Roofing &amp; Renovations – Office Banner</title>
<link rel="stylesheet" href="https://fonts.googleapis.com/css2?family=Anton&family=Alfa+Slab+One&family=Montserrat:wght@800&display=swap">
<style>
  :root {
    --brand-orange: #ff6b45;
    --ink: #050505;
    --paper: #ffffff;
    --mark-fill: #ececec;
    --backdrop: #e6e6e6;
  }
  html, body {
    margin: 0;
    width: 965px;
    height: 1200px;
    overflow: hidden;
    background: var(--backdrop);
  }
  .banner {
    position: absolute;
    left: 20px;
    top: 369px;
    width: 925px;
    height: 462.5px;
    display: block;
    box-shadow: 0 10px 24px rgba(0,0,0,0.25);
  }
  .headline { font-family: "Anton", "Impact", sans-serif; }
  .headline--first { font-size: 178px; }
  .headline--second { font-size: 200px; }
  .headline--third { font-size: 158px; }
  .headline--light { fill: var(--paper); }
  .headline--dark { fill: var(--ink); }
  .web-address { font-family: "Alfa Slab One", "Rockwell", serif; font-size: 36px; fill: var(--brand-orange); }
  .phone-number { font-family: "Montserrat", "Arial", sans-serif; font-weight: 800; font-size: 92px; fill: var(--paper); }
  .company-name, .company-line { font-family: "Montserrat", "Arial", sans-serif; font-weight: 800; fill: var(--ink); }
  .company-name { font-size: 112px; }
  .company-line { font-size: 30px; }
</style>
</head>
<body>
<svg class="banner" viewBox="0 0 1536 768" xmlns="http://www.w3.org/2000/svg" aria-label="Halven Roofing and Renovations office banner">
  <defs>
    <clipPath id="main-panel-clip">
      <path d="M0,0 H750 C815,200 790,470 590,768 H0 Z"/>
    </clipPath>
  </defs>

  <rect class="sheet" width="1536" height="768" fill="var(--paper)"/>
  <path class="contact-band" d="M790,535 C980,620 1250,650 1536,605 V768 H790 Z" fill="var(--ink)"/>

  <path class="edge-outer" d="M0,0 H833 C900,200 875,480 660,768 H0 Z" fill="var(--brand-orange)"/>
  <path class="edge-stripe" d="M0,0 H798 C862,200 838,480 625,768 H0 Z" fill="var(--paper)"/>
  <path class="headline-panel" d="M0,0 H750 C815,200 790,470 590,768 H0 Z" fill="var(--brand-orange)"/>

  <g clip-path="url(#main-panel-clip)">
    <path class="web-strip" d="M0,662 C250,645 480,650 720,680 V768 H0 Z" fill="var(--paper)"/>
    <path class="web-strip-rule" d="M0,684 C250,668 480,672 720,700" fill="none" stroke="var(--brand-orange)" stroke-width="7"/>
  </g>

  <text class="headline headline--first headline--light" x="43" y="215" textLength="668" lengthAdjust="spacingAndGlyphs">STRENGTH,</text>
  <text class="headline headline--second headline--light" x="45" y="420" textLength="608" lengthAdjust="spacingAndGlyphs">LOYALTY,</text>
  <text class="headline headline--third headline--dark" x="43" y="589" textLength="634" lengthAdjust="spacingAndGlyphs">PROTECTION</text>

  <g class="globe-icon" fill="none" stroke="var(--brand-orange)" stroke-width="3.5">
    <circle cx="59" cy="727" r="17"/>
    <ellipse cx="59" cy="727" rx="7" ry="17"/>
    <line x1="42" y1="727" x2="76" y2="727"/>
    <line x1="45" y1="718" x2="73" y2="718"/>
    <line x1="45" y1="736" x2="73" y2="736"/>
  </g>
  <text class="web-address" x="92" y="740" textLength="510" lengthAdjust="spacingAndGlyphs">www.halvenroofingtx.com</text>

  <circle class="name-disc" cx="1199" cy="210" r="170" fill="var(--mark-fill)" stroke="var(--ink)" stroke-width="10"/>
  <text class="company-name" x="979" y="522" textLength="484" lengthAdjust="spacingAndGlyphs">HALVEN</text>
  <text class="company-line" x="979" y="560" textLength="484" lengthAdjust="spacingAndGlyphs">ROOFING &amp; RENOVATIONS LLC</text>

  <rect class="phone-icon-box" x="798" y="666" width="75" height="75" rx="8" fill="var(--brand-orange)"/>
  <g class="phone-icon" fill="var(--ink)" stroke="var(--ink)">
    <path d="M817,683 l10,-4 l8,15 l-7,5 c3,9 9,16 17,20 l5,-7 l15,8 l-4,10 c-25,2 -46,-20 -44,-47 z" stroke="none"/>
    <path d="M840,688 a14,14 0 0 1 14,14" fill="none" stroke-width="3.5"/>
    <path d="M841,678 a24,24 0 0 1 23,23" fill="none" stroke-width="3.5"/>
  </g>
  <text class="phone-number" x="896" y="734" textLength="604" lengthAdjust="spacingAndGlyphs">512-555-0187</text>
</svg>
</body>
</html>
```